Website R86 coffee

I am opening a small business selling locally roasted coffee online. To start with I want a site with three pages. 1. A welcome page with logo and mission/vision. 2. Shopping/ordering page. 3. About Us page. The brand is "R86 Coffee - A warm start to every day". We are giving back to the downs syndrome community by employing people with down syndrome (Trisomy 21) and buy donating to down syndrome research.

Target Market(s)

Families and friends of people with downs syndrome

Coding

Coded - Design and coding required

Number of Pages Required

3 page

```html
<!DOCTYPE html>
<html lang="en">
<head>
<meta charset="utf-8">
<title>R86 Coffee - A warm start to every day</title>
<link href="https://fonts.googleapis.com/css2?family=Lato:wght@300;400;700&display=swap" rel="stylesheet">
<style>
  :root {
    --ink: #222222;
    --white: #ffffff;
    --accent: #f39c00;
    --button-dark: #2f2f2f;
    --panel: #f3f3f3;
    --frame: #c9c9c9;
    --muted: #555555;
    --icon: #777777;
  }
  * { margin: 0; padding: 0; box-sizing: border-box; }
  html, body { width: 1200px; height: 2260px; overflow: hidden; }
  body { font-family: 'Lato', sans-serif; color: var(--ink); background: var(--white); position: relative; }

  .hero {
    position: absolute; left: 0; top: 0; width: 1200px; height: 818px;
    background: radial-gradient(ellipse at 55% 60%, #7a4a2a 0%, #4e2e19 45%, #2b1a10 100%);
  }
  .brand {
    position: absolute; left: 76px; top: 48px; width: 332px; height: 94px;
    background: var(--white); border: 3px solid #111;
    display: flex; align-items: center; justify-content: center; gap: 14px;
  }
  .brand-mark { width: 18px; height: 18px; background: var(--ink); }
  .brand-name { font-size: 40px; font-weight: 300; letter-spacing: 2px; color: var(--ink); }
  .main-nav { position: absolute; top: 82px; right: 73px; display: flex; gap: 76px; }
  .main-nav a { color: var(--white); text-decoration: none; font-size: 19px; letter-spacing: 0.5px; }
  .hero-title {
    position: absolute; left: 0; width: 1200px; top: 366px; text-align: center;
    color: var(--white); font-size: 88px; font-weight: 400; letter-spacing: 3px; line-height: 1;
  }
  .hero-tagline {
    position: absolute; left: 0; width: 1200px; top: 462px; text-align: center;
    color: var(--white); font-size: 40px; font-weight: 400;
  }
  .btn {
    position: absolute; display: flex; align-items: center; justify-content: center;
    color: var(--white); font-size: 19px; letter-spacing: 0.5px; text-decoration: none;
  }
  .hero .btn { left: 500px; top: 538px; width: 180px; height: 62px; background: #050505; }

  .section-title { position: absolute; left: 0; width: 1200px; top: 884px; text-align: center; font-size: 44px; font-weight: 300; letter-spacing: 2px; }
  .statement { position: absolute; left: 77px; width: 520px; }
  .statement h3 { color: var(--accent); font-size: 28px; font-weight: 700; line-height: 1; margin-bottom: 10px; }
  .statement p { font-size: 21px; line-height: 37px; }
  .vision { top: 978px; }
  .mission { top: 1152px; }
  .mission-photo {
    position: absolute; left: 615px; top: 980px; width: 512px; height: 555px;
    background: linear-gradient(135deg, #c7b29a 0%, #9c7d62 40%, #3c5f8a 75%, #e8e6e2 100%);
  }
  .donate { left: 77px; top: 1471px; width: 192px; height: 62px; background: var(--button-dark); }

  .about { position: absolute; left: 0; top: 1617px; width: 1200px; height: 505px; background: var(--panel); }
  .about-photo {
    position: absolute; left: 0; top: 0; width: 587px; height: 505px;
    background: linear-gradient(160deg, #2c3236 0%, #1a1d20 50%, #5a4634 100%);
  }
  .about-frame { position: absolute; left: 405px; top: 59px; width: 722px; height: 387px; border: 2px solid var(--frame); }
  .about-copy { position: absolute; left: 632px; top: 90px; width: 480px; }
  .about-copy h2 { font-size: 44px; font-weight: 300; letter-spacing: 1px; line-height: 1; margin-bottom: 16px; }
  .about-copy p { font-size: 17.5px; line-height: 31.4px; }
  .about .btn { left: 632px; top: 346px; width: 179px; height: 62px; background: var(--button-dark); }

  .site-footer { position: absolute; left: 0; top: 2168px; width: 1200px; text-align: center; }
  .site-footer p { font-size: 15px; color: var(--muted); }
  .social { display: flex; justify-content: center; gap: 18px; margin-top: 18px; }
  .social span { width: 18px; height: 18px; border-radius: 50%; background: var(--icon); display: block; }
</style>
</head>
<body>
  <header class="hero" role="img" aria-label="Photo of hands scooping freshly roasted coffee beans in a roaster">
    <div class="brand"><span class="brand-mark"></span><span class="brand-name">R86 COFFEE</span></div>
    <nav class="main-nav">
      <a href="#">HOME</a>
      <a href="#">ABOUT US</a>
      <a href="#">SHOPPING</a>
    </nav>
    <h1 class="hero-title">R86 COFFEE</h1>
    <p class="hero-tagline">A warm start to every day</p>
    <a class="btn" href="#">READ MORE</a>
  </header>

  <h2 class="section-title">VISION &amp; MISSION</h2>
  <div class="statement vision">
    <h3>VISION</h3>
    <p>Develop a company that markets coffee and related products to family and friends of the down syndrome community.</p>
  </div>
  <div class="statement mission">
    <h3>MISSION</h3>
    <p>Create and grow an online company selling contract roasted coffee. As growth permits become a fully vertically integrated coffee company from roasting to our own coffee shop. The company will give significant funds to medical research in downs syndrome and we will hire as many people with downs syndrome as possible.</p>
  </div>
  <a class="btn donate" href="#">BUY DONATING</a>
  <div class="mission-photo" role="img" aria-label="Photo of a mother pouring coffee for her smiling daughter at a table"></div>

  <section class="about">
    <div class="about-photo" role="img" aria-label="Photo of a roaster working at a coffee roasting machine"></div>
    <div class="about-frame"></div>
    <div class="about-copy">
      <h2>ABOUT US</h2>
      <p>Sed ut perspiciatis unde omnis iste natus error sit voluptatem accusantium doloremque laudantium, totam rem aperiam, eaque ipsa quae ab illo inventore veritatis et quasi architecto beatae vitae dicta sunt explicabo mo enim ipsam voluptatem quia voluptas sit aspernatur aut odit aut fugit,.</p>
    </div>
    <a class="btn" href="#">READ MORE</a>
  </section>

  <footer class="site-footer">
    <p>Copyright© 2021. Company Name.All Right Reserved</p>
    <div class="social" aria-label="Social links">
      <span></span><span></span><span></span><span></span><span></span><span></span>
    </div>
  </footer>
</body>
</html>
```